Bramblewick Dill Pickles needs your smart gourmet Design

Looking for a smart design for a dill pickle jar container. The text
Bramblewick Dill Pickles.
Simply Picklelicious.

A tasty reason to raid the refrigerator.

Target Market(s)

Foodies, farmers market types.

Font styles to use
Serif
Sans Serif

Colors

Designer to choose colors to be used in the design.

Requirements
Must have
• Attractive design to entice foodies to buy my Pickles. Not cluttered, easy to read.
Nice to have
• Pickles, garlic. Modern.
Should not have
• Clutter. No script text.

```html
<!DOCTYPE html>
<html lang="en">
<head>
<meta charset="utf-8">
<title>Bramblewick Dill Pickles – Jar Label</title>
<link rel="stylesheet" href="https://fonts.googleapis.com/css2?family=Libre+Baskerville:wght@700&family=Open+Sans:wght@400;700&display=swap">
<style>
  :root {
    --canvas-bg: #e9e7e4;
    --label-dark: #25381f;
    --label-mid: #3e5b36;
    --border-green: #139433;
    --border-white: #ffffff;
    --lime: #c5da3a;
    --text-white: #ffffff;
    --garlic-light: #f4f2ee;
    --garlic-shade: #cfcac2;
    --bomb-green: #4f9a2b;
  }
  html, body {
    margin: 0;
    padding: 0;
    width: 1060px;
    height: 1200px;
    overflow: hidden;
    background: var(--canvas-bg);
  }
  .canvas {
    position: relative;
    width: 1060px;
    height: 1200px;
  }
  .jar-label {
    position: absolute;
    left: 70px;
    top: 50px;
    width: 920px;
    height: 1100px;
  }
  .label-title {
    font-family: "Libre Baskerville", Georgia, serif;
    font-weight: 700;
    fill: var(--text-white);
    text-transform: uppercase;
  }
  .label-sans {
    font-family: "Open Sans", Arial, sans-serif;
  }
  .quality { font-weight: 700; font-size: 34px; fill: var(--text-white); }
  .tagline { font-weight: 700; font-size: 37px; fill: var(--lime); }
  .slogan { font-weight: 400; font-size: 30px; fill: var(--text-white); }
  .stars { fill: var(--text-white); }
</style>
</head>
<body>
<main class="canvas">
  <svg class="jar-label" viewBox="0 0 920 1100" xmlns="http://www.w3.org/2000/svg">
    <defs>
      <radialGradient id="label-fill" cx="75%" cy="55%" r="80%">
        <stop offset="0" stop-color="var(--label-mid)"/>
        <stop offset="1" stop-color="var(--label-dark)"/>
      </radialGradient>
      <radialGradient id="garlic-fill" cx="50%" cy="45%" r="55%">
        <stop offset="0" stop-color="var(--garlic-light)"/>
        <stop offset="0.7" stop-color="var(--garlic-shade)"/>
        <stop offset="1" stop-color="var(--garlic-shade)" stop-opacity="0"/>
      </radialGradient>
      <path id="title-arc" d="M100,335 Q460,165 820,335"/>
      <path id="subtitle-arc" d="M190,415 Q460,325 730,415"/>
    </defs>

    <path class="label-border-outer" fill="none" stroke="var(--border-white)" stroke-width="30"
      d="M0,160 H200 C250,160 250,60 330,30 C400,5 520,5 590,30 C670,60 670,160 720,160 H920 V940 H720 C670,940 670,1040 590,1070 C520,1095 400,1095 330,1070 C250,1040 250,940 200,940 H0 Z"/>
    <path class="label-body" fill="url(#label-fill)" stroke="var(--border-green)" stroke-width="14"
      d="M0,160 H200 C250,160 250,60 330,30 C400,5 520,5 590,30 C670,60 670,160 720,160 H920 V940 H720 C670,940 670,1040 590,1070 C520,1095 400,1095 330,1070 C250,1040 250,940 200,940 H0 Z"/>

    <g class="stars">
      <path d="M418,52 l5,12 h13 l-10,8 4,13 -12,-8 -12,8 4,-13 -10,-8 h13z"/>
      <path d="M460,48 l5,12 h13 l-10,8 4,13 -12,-8 -12,8 4,-13 -10,-8 h13z"/>
      <path d="M502,52 l5,12 h13 l-10,8 4,13 -12,-8 -12,8 4,-13 -10,-8 h13z"/>
    </g>
    <text class="label-sans quality" x="460" y="140" text-anchor="middle">Best Quality</text>
    <rect class="quality-rule" x="350" y="155" width="220" height="4" fill="var(--lime)"/>

    <text class="label-title" font-size="78">
      <textPath href="#title-arc" startOffset="50%" text-anchor="middle">Bramblewick</textPath>
    </text>
    <text class="label-title" font-size="56">
      <textPath href="#subtitle-arc" startOffset="50%" text-anchor="middle">Dill Pickles</textPath>
    </text>

    <text class="label-sans tagline" x="460" y="485" text-anchor="middle">Simply Picklelicious.</text>

    <g role="img" aria-label="Illustration of garlic bulbs with a parsley sprig">
      <ellipse cx="410" cy="715" rx="230" ry="160" fill="url(#garlic-fill)"/>
    </g>
    <g role="img" aria-label="Small cartoon bomb icon">
      <circle cx="620" cy="598" r="42" fill="var(--bomb-green)"/>
    </g>

    <text class="label-sans slogan" x="460" y="930" text-anchor="middle">A tasty reason to</text>
    <text class="label-sans slogan" x="460" y="982" text-anchor="middle">raid the refrigerator.</text>
  </svg>
</main>
</body>
</html>
```